Wageline Associates Business Card Design

We need a business card designed around our new logo. The business card should be modern in design & should communicate success, confidence, power, sophistication. The target market is young business professionals. This is for a human resource & payroll outsourcing business.

```html
<!DOCTYPE html>
<html lang="en">
<head>
<meta charset="utf-8">
<title>Wageline Associates Business Card</title>
<link href="https://fonts.googleapis.com/css2?family=Open+Sans:wght@400;600;700&display=swap" rel="stylesheet">
<style>
  :root {
    --bg: #d9d9d9;
    --card-dark: #2b2b2b;
    --card-light: #f4f4f4;
    --card-light-end: #e6e6e6;
    --red: #b7282e;
    --ink: #1e1e1e;
    --muted: #9a9a9a;
    --white: #ffffff;
  }
  * { box-sizing: border-box; margin: 0; padding: 0; }
  html, body { width: 1200px; height: 1021px; overflow: hidden; }
  body {
    background: var(--bg);
    font-family: "Open Sans", sans-serif;
    position: relative;
  }
  .card {
    position: absolute;
    width: 700px;
    height: 400px;
    border-radius: 3px;
    box-shadow: 0 10px 30px rgba(0,0,0,0.25);
    overflow: hidden;
  }
  /* Back side */
  .card-back {
    left: 320px;
    top: 60px;
    background: var(--card-dark);
  }
  .card-back .brand {
    position: absolute;
    left: 0; right: 0;
    top: 150px;
    display: flex;
    justify-content: center;
    align-items: center;
    gap: 14px;
  }
  .brand-dot {
    width: 22px; height: 22px;
    border-radius: 50%;
    background: var(--red);
    flex: none;
  }
  .brand-name {
    font-weight: 600;
    font-size: 42px;
    letter-spacing: 0.5px;
    line-height: 1;
  }
  .card-back .brand-name { color: var(--white); }
  .card-back .web {
    position: absolute;
    left: 0; right: 0;
    bottom: 62px;
    text-align: center;
    font-size: 15px;
    letter-spacing: 3px;
    color: var(--white);
  }
  .card-back .web .accent { color: var(--red); }

  /* Front side */
  .card-front {
    left: 200px;
    top: 540px;
    background: linear-gradient(135deg, var(--card-light), var(--card-light-end));
  }
  .card-front .brand {
    position: absolute;
    left: 40px;
    top: 150px;
    width: 300px;
    display: flex;
    align-items: center;
    gap: 12px;
  }
  .card-front .brand-name {
    color: var(--ink);
    font-size: 27px;
  }
  .divider {
    position: absolute;
    left: 360px;
    top: 80px;
    width: 1px;
    height: 190px;
    background: var(--muted);
  }
  .contact {
    position: absolute;
    left: 385px;
    top: 88px;
    color: var(--ink);
  }
  .person-name {
    color: var(--red);
    font-weight: 700;
    font-size: 22px;
    line-height: 1.1;
  }
  .person-role {
    font-size: 16px;
    margin-bottom: 18px;
  }
  .address { font-size: 16px; line-height: 1.35; }
  .contact-line {
    display: flex;
    align-items: center;
    gap: 8px;
    font-size: 16px;
    line-height: 1.4;
  }
  .contact-line svg { flex: none; }
  .bands {
    position: absolute;
    left: 0; bottom: 0;
  }
  .band-web {
    position: absolute;
    right: 40px;
    bottom: 14px;
    color: var(--white);
    font-size: 17px;
    letter-spacing: 0.5px;
  }
</style>
</head>
<body>

  <section class="card card-back" aria-label="Card back">
    <div class="brand">
      <span class="brand-dot"></span>
      <span class="brand-name">Wageline Associates</span>
    </div>
    <p class="web">www.<span class="accent">wagelineassociates</span>.com</p>
  </section>

  <section class="card card-front" aria-label="Card front">
    <div class="brand">
      <span class="brand-dot"></span>
      <span class="brand-name">Wageline Associates</span>
    </div>

    <div class="divider"></div>

    <div class="contact">
      <p class="person-name">Daniel Harper</p>
      <p class="person-role">President</p>
      <p class="address">240 N. W. 5th Street<br>Tampa, Florida, 33602</p>
      <p class="contact-line">
        <svg width="14" height="14" viewBox="0 0 24 24" aria-hidden="true">
          <path fill="#b7282e" d="M6.6 10.8a15.1 15.1 0 0 0 6.6 6.6l2.2-2.2c.3-.3.7-.4 1-.2 1.1.4 2.3.6 3.6.6.6 0 1 .4 1 1V20c0 .6-.4 1-1 1A17 17 0 0 1 3 4c0-.6.4-1 1-1h3.5c.6 0 1 .4 1 1 0 1.3.2 2.5.6 3.6.1.3 0 .7-.2 1z"/>
        </svg>
        (123) 555-0187
      </p>
      <p class="contact-line">
        <svg width="15" height="12" viewBox="0 0 20 14" aria-hidden="true">
          <rect x="1" y="1" width="18" height="12" fill="none" stroke="#b7282e" stroke-width="1.8"/>
          <path d="M1 1l9 7 9-7M1 13l7-6M19 13l-7-6" fill="none" stroke="#b7282e" stroke-width="1.5"/>
        </svg>
        daniel@wagelineassociates.com
      </p>
    </div>

    <svg class="bands" width="700" height="70" viewBox="0 0 700 70" aria-hidden="true">
      <polygon points="0,36 330,58 320,70 0,70" fill="#2b2b2b"/>
      <path d="M320 70 L345 28 Q352 16 370 16 L700 16 L700 70 Z" fill="#b7282e"/>
    </svg>
    <p class="band-web">www.wagelineassociates.com</p>
  </section>

</body>
</html>
```